cartNest - a stylish trolley for apartments

We neede a simple website to sell our Trolley, for apartment use.
The colour theme is red, blask & white. Our logo is attached and this needs to be on the Home page.
The website only needs a Home Page plus 4 other pges.
In the attachment you will find a site map.

You can check out the following two sites to see what I like:
www.plinthgallery.example/design-showcase-inspiration/minimalist-portfolio-website/
www.brightquarry.example/inspiration/40-beautiful-web-design-portfolios/ in this site especially
Dario Menezes
K B Forge
Nine 17 Studio
Oliver Marsh

And especially Lamp - I ike the simpicity of the site esp as we are only selling one product

Target Market(s)

Apartment dwellers

Industry/Entity Type

Apartment

Requirements
Must have
• This website must have 4 pages.
We need Corvo, Ledgerline and Quidly portals.
Order Form for Trolley
Payment form.

```html
<!DOCTYPE html>
<html lang="en">
<head>
<meta charset="utf-8">
<title>cartNest – a stylish trolley for apartments</title>
<link href="https://fonts.googleapis.com/css2?family=Source+Sans+3:wght@400;600;700&family=Arimo:wght@700&family=Gochi+Hand&display=swap" rel="stylesheet">
<style>
  :root{
    --page:#f2f1f1;
    --panel:#ffffff;
    --red:#c8161d;
    --ink:#2b2b2b;
    --body:#6b6b6b;
    --muted:#8a8a8a;
    --line:#dcdcdc;
  }
  *{box-sizing:border-box;margin:0;padding:0}
  html,body{width:1145px;height:1200px;overflow:hidden}
  body{background:var(--page);font-family:"Source Sans 3",sans-serif;color:var(--body);position:relative}
  .abs{position:absolute}

  /* brand */
  .brand{left:51px;top:156px;display:flex;align-items:center;gap:8px}
  .brand-dot{width:18px;height:18px;border-radius:50%;background:var(--red)}
  .brand-name{font-size:38px;font-weight:700;color:var(--ink);letter-spacing:-1px;line-height:1}

  /* utility bar */
  .utility{top:37px;left:566px;display:flex;gap:24px;font-size:13px;color:var(--ink)}
  .utility span{display:flex;align-items:center;gap:6px}
  .utility svg{width:13px;height:13px;fill:var(--ink)}
  .search{left:933px;top:32px;width:164px;height:27px;border:1px solid #cfcfcf;border-radius:3px;background:#fff;box-shadow:inset 0 1px 2px rgba(0,0,0,.08);font-size:12px;font-style:italic;color:#aaa;padding:6px 14px}
  .search svg{position:absolute;right:8px;top:7px;width:12px;height:12px}

  /* main nav */
  .nav{top:96px;left:0;width:1145px;height:20px;font-size:15px;color:var(--ink)}
  .nav a{position:absolute;text-decoration:none;color:inherit}
  .nav a.current{color:var(--red)}
  .nav-rule{left:221px;top:137px;width:877px;height:4px;background:var(--red)}
  .nav-mark{left:598px;top:126px;width:0;height:0;border-left:9px solid transparent;border-right:9px solid transparent;border-bottom:11px solid var(--red)}

  .panel{background:var(--panel);border-radius:9px}

  /* intro */
  .intro{left:50px;top:218px;width:1044px;height:319px}
  .intro-copy{left:83px;top:254px;width:760px;font-size:13.6px;line-height:21.8px}
  .intro-copy p{margin-bottom:10.8px}
  .intro-copy b{color:var(--red);font-weight:700}
  .hero-photo{left:850px;top:191px;width:251px;height:403px;border-radius:8px;background:linear-gradient(180deg,#e9e3d6 0%,#c4ad7a 40%,#9a8268 75%,#7a3a2a 100%)}

  .section-title{font-family:"Arimo",sans-serif;font-weight:700;font-size:21px;color:var(--ink)}
  .section-title em{font-style:normal;color:var(--red)}

  /* gallery */
  .gallery-title{left:335px;top:574px}
  .gallery{left:300px;top:611px;width:794px;height:276px}
  .gallery-copy{left:364px;top:641px;width:700px;font-size:13.6px;line-height:21.8px;text-align:justify}
  .thumb{top:755px;width:182px;height:104px;border-radius:10px;border:2px solid #d5d5d5;background:linear-gradient(180deg,#d9c77a 0%,#8a8a7a 45%,#3a3a3a 100%)}
  .polaroid{left:54px;top:584px;width:282px;height:307px;background:#fafafa;border:1px solid #ddd;box-shadow:0 4px 10px rgba(0,0,0,.25);transform:rotate(-2deg)}
  .polaroid-photo{position:absolute;left:15px;top:18px;width:252px;height:247px;background:linear-gradient(180deg,#cfd2d4 0%,#9ea3a6 55%,#3d3d3d 85%,#2a2a2a 100%)}
  .polaroid-caption{position:absolute;left:0;right:0;top:268px;text-align:center;font-family:"Gochi Hand",cursive;font-size:22px;color:#555}

  /* contact */
  .contact-title{left:84px;top:913px}
  .contact{left:50px;top:950px;width:1044px;height:145px}
  .contact-icon{left:100px;top:972px;width:104px;height:100px}
  .contact-list{font-size:13.6px;line-height:21.8px;color:var(--body)}
  .contact-list dt{position:absolute;left:0}
  .contact-list dd{margin-left:var(--indent)}
  .address{left:252px;top:987px;--indent:77px}
  .phones{left:547px;top:987px;--indent:54px}
  .connect{left:777px;top:987px;font-size:13.6px}
  .socials{left:778px;top:1022px;display:flex;gap:20px}
  .socials span{width:24px;height:24px;border-radius:3px;display:block}

  /* footer */
  .footer-links{top:1126px;left:0;width:1145px;text-align:center;font-size:13px;color:var(--ink)}
  .footer-links span{margin:0 6px}
  .copyright{top:1150px;left:0;width:1145px;text-align:center;font-size:13px;color:var(--ink)}
</style>
</head>
<body>

<header>
  <div class="brand abs">
    <span class="brand-dot"></span>
    <span class="brand-name">cartNest</span>
  </div>

  <div class="utility abs">
    <span><svg viewBox="0 0 16 16"><path d="M1 2h3l2 8h8l1.5-6H5.3" fill="none" stroke="#2b2b2b" stroke-width="1.6"/><circle cx="7" cy="13.5" r="1.4"/><circle cx="13" cy="13.5" r="1.4"/></svg>My Cart &nbsp;- &nbsp;(0) Items</span>
    <span><svg viewBox="0 0 16 16"><circle cx="8" cy="5" r="3.6"/><path d="M1 16c0-4 3.2-6.5 7-6.5s7 2.5 7 6.5z"/></svg>My Account</span>
    <span><svg viewBox="0 0 16 16"><rect x="1.5" y="2.5" width="11" height="11" fill="none" stroke="#2b2b2b" stroke-width="1.6"/><path d="M4 7l3 3 7-8" fill="none" stroke="#2b2b2b" stroke-width="2"/></svg>Check out</span>
  </div>

  <div class="search abs">Search
    <svg viewBox="0 0 12 12"><circle cx="5" cy="5" r="3.5" fill="none" stroke="#bbb" stroke-width="1.4"/><path d="M7.5 7.5l3.5 3.5" stroke="#bbb" stroke-width="1.6"/></svg>
  </div>

  <nav class="nav abs">
    <a class="current" style="left:568px">cartNest</a>
    <a style="left:694px">Gallery</a>
    <a style="left:800px">Contact Us</a>
    <a style="left:931px">My Cart</a>
    <a style="left:1012px">Login</a>
  </nav>
  <div class="nav-mark abs"></div>
  <div class="nav-rule abs"></div>
</header>

<main>
  <section>
    <div class="intro panel abs"></div>
    <div class="intro-copy abs">
      <p><b>cartNest</b> evolved from demand! &nbsp;Apartment dwellers everywhere are calling for a solution to moving shopping, luggage and other goods from car to apartment, and vice versa. Other trolleys on the market are not versatile, they are not robust, but more importantly, they are NOT stylish! The emphasis of <b>cartNest</b> is on style. This trolley is stylish enough to remain in your apartment as a piece of furniture. It features a versatile flat-bed and hanger, to cope with all your transport needs.</p>
      <p>IT LOOKS GREAT! &nbsp;Designed along the lines of the familiar hotel “birdcage” luggage trolley, it provides smart and practical use for all small transport needs. &nbsp;The stylish trolley does not need to be disassembled and stored away in a cupboard or storage area. It can live in the apartment, proudly! &nbsp;Trolleys with plastic coated wire baskets soon become shabby and chipped.</p>
      <p><b>cartNest</b> is made of high quality stainless steel and other robust materials. Whilst other trolleys tend to look like they belong in a factory or workshop, <b>cartNest</b> is the classy alternative, which can live anywhere in your apartment, and not in the cupboard.</p>
      <p>So – we welcome <b>cartNest</b> to the marketplace!</p>
    </div>
    <div class="hero-photo abs" role="img" aria-label="Brass birdcage luggage trolley with red base carrying stacked suitcases"></div>
  </section>

  <section>
    <h2 class="section-title gallery-title abs"><em>Our</em> Gallery</h2>
    <div class="gallery panel abs"></div>
    <p class="gallery-copy abs">Sed ut perspiciatis unde omnis iste natus error sit voluptatem accusantium doloremque laudantium, totam rem aperiam, eaque ipsa quae ab illo inventore veritatis et quasi architecto beatae vitae dicta sunt explicabo. Nemo enim ipsam voluptatem quia voluptas sit aspernatur aut odit aut fugit, sed quia consequuntur magni dolores eos qui ratione voluptatem sequi nesciunt.</p>
    <div class="thumb abs" style="left:386px" role="img" aria-label="Loading bags from a car boot onto the trolley in a parking garage"></div>
    <div class="thumb abs" style="left:616px" role="img" aria-label="Trolley beside an open car in an underground car park"></div>
    <div class="thumb abs" style="left:846px" role="img" aria-label="Trolley loaded with luggage next to a white car"></div>
    <figure class="polaroid abs">
      <div class="polaroid-photo" role="img" aria-label="Trolley with red suitcases and hanging garments in a lift lobby"></div>
      <figcaption class="polaroid-caption">Trolley</figcaption>
    </figure>
  </section>

  <section>
    <h2 class="section-title contact-title abs"><em>Contact</em> Us</h2>
    <div class="contact panel abs"></div>
    <svg class="contact-icon abs" viewBox="0 0 104 100" aria-hidden="true">
      <path d="M52 6C26 6 8 22 8 42c0 12 6 22 16 28l-6 20 22-14c4 1 8 1 12 1 26 0 44-16 44-35S78 6 52 6z" fill="#f4f4f4" stroke="#c9c9c9" stroke-width="3"/>
      <path d="M36 24c4-2 7 0 9 5l2 6c1 3-1 5-3 6 2 6 6 10 12 12 1-2 3-4 6-3l6 2c5 2 7 5 5 9-3 5-8 7-14 5-13-4-24-15-28-28-2-6 0-11 5-14z" fill="#1f6fb5"/>
    </svg>
    <dl class="contact-list address abs">
      <dt>Address :</dt>
      <dd>Neque porro quisquam,<br>dolorem ipsum<br>numquam- D45S3</dd>
    </dl>
    <dl class="contact-list phones abs">
      <dt>Phone :</dt><dd>456 210 7731</dd>
      <dt>Fax &nbsp;&nbsp;&nbsp;:</dt><dd>456 210 7732</dd>
      <dt>E mail :</dt><dd>info@cartnest.example</dd>
    </dl>
    <div class="connect abs">Connect with us :</div>
    <div class="socials abs">
      <span style="background:#3b5a96" aria-label="Social network 1"></span>
      <span style="background:#6cc3e8" aria-label="Social network 2"></span>
      <span style="background:#e9662b" aria-label="Social network 3"></span>
      <span style="background:#1f6fa8" aria-label="Social network 4"></span>
      <span style="background:#4a9a3d" aria-label="Social network 5"></span>
    </div>
  </section>
</main>

<footer>
  <div class="footer-links abs">cartNest<span>|</span>Gallery<span>|</span>Contact Us<span>|</span>My Cart<span>|</span>Login</div>
  <div class="copyright abs">Copyright © 2012 www.cartnest.example &nbsp;All rights reserved.</div>
</footer>

</body>
</html>
```